"Autumn Special" 6 Month Membership Special

Running a Membership Drive on a 6 month membership option for the month of April/May. 6 months $150.00 save 50%. Below is recent ads made from designers on Vellum Forge to assist. Final design should be inviting / colorful and eye catching

Format required is for a Facebook cover, Instagram, and A0 format for a poster .

Target Market(s)

16-40 male and female

Industry/Entity Type

Fitness

Font styles to use
Serif
Other font styles liked:
• Athletic

Colors

Designer to choose colors to be used in the design.

Requirements
Must have
• The main emphasis would be on the "6 MONTH SPECIAL" or "AUTUMN SPECIAL" font/text (special) and the layout of the text. If we can add some brighter colors to the layout that would be great just to capture their attention. If there's any effects you want to add to it that would be great. The logo can be faint in the background. The image of the female model can some some artistic effects around it and she does not have to be the main focus
• "AUTUMN SPECIAL"
• 6 MONTHS from
• $150.00
• SAVE 50%"
• "Terms and conditions apply"
• All contact details, address, website, etc which will be supplied
Nice to have
• Some artistic effects to catch your eye and enhance the professionalism of the designer. Attached is a "Athletic font" Logo which that style could be incorporated
Should not have
• You don't have to include the orange background of the female model, you can use her silhouette

```html
<!DOCTYPE html>
<html lang="en">
<head>
<meta charset="UTF-8">
<title>Autumn Special – Ironpeak Gym</title>
<link rel="stylesheet" href="https://fonts.googleapis.com/css2?family=Anton&family=Roboto+Condensed:wght@400;700&display=swap">
<style>
  :root {
    --page-bg: #e6e6e6;
    --green: #4f9a3c;
    --yellow: #f4b81c;
    --orange: #ef7f1c;
    --red: #e0232a;
    --cream: #fbf1d0;
    --gold: #d9b25a;
    --ink: #1c1c1a;
    --tag-red: #d8262f;
    --tag-lime: #b9c83a;
    --white: #ffffff;
  }
  * { margin: 0; padding: 0; box-sizing: border-box; }
  html, body { width: 1200px; height: 1200px; overflow: hidden; background: var(--page-bg); }
  .flyer {
    position: absolute; left: 136px; top: 0; width: 928px; height: 1200px; overflow: hidden;
    background: linear-gradient(180deg, var(--green) 0%, #9fae2a 18%, var(--yellow) 38%, var(--orange) 70%, var(--red) 100%);
    font-family: "Roboto Condensed", sans-serif;
  }
  .headline {
    position: absolute; left: 0; width: 928px; top: 68px; text-align: center;
    font-family: "Anton", sans-serif; font-size: 108px; line-height: 1; letter-spacing: 1px;
    color: var(--cream); text-shadow: 0 4px 6px rgba(60,40,0,.45);
  }
  .price-band {
    position: absolute; left: 90px; top: 186px; width: 760px; height: 70px;
    background: radial-gradient(ellipse at center, rgba(20,22,10,.85) 0%, rgba(20,22,10,.55) 60%, rgba(20,22,10,0) 100%);
  }
  .price-line {
    position: absolute; left: 0; width: 928px; top: 188px; text-align: center;
    font-weight: 700; font-size: 62px; line-height: 66px; color: var(--cream);
  }
  .athlete-photo {
    position: absolute; left: 10px; top: 385px; width: 440px; height: 750px;
    background: radial-gradient(ellipse at 50% 45%, rgba(70,75,80,.55) 0%, rgba(70,75,80,.25) 45%, rgba(70,75,80,0) 72%);
  }
  .offer-ribbon { position: absolute; left: 0; top: 0; width: 928px; height: 1200px; }
  .gym-badge { position: absolute; left: 556px; top: 780px; width: 300px; height: 300px; }
  .contact-line {
    position: absolute; left: 0; width: 928px; top: 1124px; text-align: center;
    font-weight: 700; font-size: 27px; color: var(--white);
  }
</style>
</head>
<body>
  <main class="flyer">
    <h1 class="headline">AUTUMN SPECIAL</h1>
    <div class="price-band"></div>
    <p class="price-line">6 MONTHS FROM - $150.00</p>

    <div class="athlete-photo" role="img" aria-label="Photo of a female athlete running with dumbbells in grey sportswear"></div>

    <svg class="offer-ribbon" viewBox="0 0 928 1200" aria-hidden="false">
      <polygon points="469,560 544,600 544,670 679,762 469,665" fill="var(--ink)"/>
      <polygon points="544,570 929,480 929,620 544,672" fill="var(--tag-lime)" opacity=".85"/>
      <polygon points="469,430 857,288 857,500 469,620" fill="var(--ink)" opacity=".92"/>
      <polygon points="402,380 680,322 718,352 402,440" fill="var(--tag-red)"/>
      <text x="549" y="385" transform="rotate(-12 549 385)" text-anchor="middle"
            font-family="Roboto Condensed, sans-serif" font-size="28" fill="var(--cream)">MEMBERSHIP SPECIAL</text>
      <text x="662" y="468" transform="rotate(-15 662 468)" text-anchor="middle"
            font-family="Anton, sans-serif" font-size="84" fill="var(--gold)">SAVE 50%</text>
      <text x="740" y="580" transform="rotate(-14 740 580)" text-anchor="middle"
            font-family="Roboto Condensed, sans-serif" font-size="23" fill="var(--ink)">TERMS AND CONDITIONS APPLY</text>
    </svg>

    <svg class="gym-badge" viewBox="0 0 300 300">
      <circle cx="150" cy="150" r="142" fill="none" stroke="var(--white)" stroke-width="8"/>
      <text x="150" y="140" text-anchor="middle" font-family="Roboto Condensed, sans-serif"
            font-weight="700" font-size="52" fill="var(--white)">IRONPEAK</text>
      <text x="150" y="198" text-anchor="middle" font-family="Roboto Condensed, sans-serif"
            font-weight="700" font-size="52" fill="var(--white)">GYM</text>
    </svg>

    <p class="contact-line">FOR MORE INFO :-&nbsp; 555 0142 786 | WWW.IRONPEAKFITNESS.COM</p>
  </main>
</body>
</html>
```